Redesign Website for Tandara Flame

I have an existing website on https://www.tandaraflame-example.com.au/ and would like to have this redesigned professionally with new content (please refer to word document). We are fire protection engineers providing fire services design expertise and engineering design to a range of different clients.

We also provide drafting services to clients in the form of completing final commissioning documentation such as 'as-installed' drawings and fire services block plans to ensure compliance with the building code and relevant Australian Standards.

Target Market(s)

Builders, Architects, Consultants, Project Managers

Industry/Entity Type

Engineering Consultant

Coding

Coded - Design and coding required

Number of Pages Required

4 page

Font styles to use
Sans Serif

Requirements
Must have
• Home and about Page, fire services design page, fire block plans page, contact us page (4 Pages).

The website colour choice must match or compliment the new company logo.
Nice to have
• Quality photos of fire services installations in buildings to Australian Standards.

A website similar to this would be ideal http://corbellpyro-example.com.au
Should not have
• Stolen licensed photos

```html
<!DOCTYPE html>
<html lang="en">
<head>
<meta charset="utf-8">
<title>Tandara Flame — Fire Services Design</title>
<link href="https://fonts.googleapis.com/css2?family=Poppins:wght@400;500;600;700;800&family=Montserrat:wght@600;700&family=Russo+One&display=swap" rel="stylesheet">
<style>
:root{
  --orange:#f7931e;
  --orange-deep:#ef7f12;
  --ink:#111111;
  --text:#444444;
  --muted:#8a8a8a;
  --white:#ffffff;
  --footer:#161616;
  --line:#3a3a3a;
}
*{margin:0;padding:0;box-sizing:border-box}
html,body{width:1200px;height:3098px;overflow:hidden}
body{font-family:"Poppins",sans-serif;color:var(--text);background:var(--white);position:relative}
.abs{position:absolute}
.center{text-align:center}

/* top bar */
.topbar{left:278px;top:0;width:862px;height:38px;background:var(--ink);color:var(--white);font-size:11.5px;display:flex;align-items:center;justify-content:flex-end;white-space:nowrap}
.topbar::before{content:"";position:absolute;left:-18px;top:0;border-top:38px solid var(--ink);border-left:18px solid transparent}
.topbar .item{height:38px;display:flex;align-items:center;gap:9px;padding:0 16px;border-left:1px solid #444}
.topbar .item:last-child{border-right:1px solid #444;padding:0 8px}
.topbar .item b{font-weight:600}
.ico-hex{width:26px;height:26px;border-radius:50%;background:var(--orange);display:flex;align-items:center;justify-content:center;flex:none}
.social{display:flex;gap:10px}
.social span{width:28px;height:28px;border-radius:50%;background:#2d6fb7;display:block}
.social span:nth-child(2){background:#2aa3e8}
.social span:nth-child(3){background:#1a86c7}

/* header */
.logo{display:flex;align-items:center;gap:10px}
.logo .dot{width:30px;height:30px;border-radius:50%;background:var(--orange)}
.logo .name{font-family:"Poppins",sans-serif;font-weight:600;font-size:19px;color:var(--orange);letter-spacing:.5px;text-transform:uppercase;white-space:nowrap}
.nav{top:68px;left:563px;display:flex;gap:33px;font-size:12px;color:#8d8d8d;letter-spacing:.4px;white-space:nowrap}
.nav .active{color:var(--orange);font-weight:600}
.nav-mark{left:576px;top:89px;width:10px;height:10px;border:2px solid var(--orange);border-radius:50%}
.search{left:1124px;top:68px}

/* hero */
.hero{left:0;top:112px;width:1200px;height:638px;background:linear-gradient(90deg,#f4f4f4 0%,#ececec 45%,#dcdcdc 100%)}
.hero-photo{left:480px;top:112px;width:720px;height:638px;background:linear-gradient(100deg,rgba(236,236,236,0) 0%,#c9ccd3 20%,#3e5a8a 48%,#d7d9dc 62%,#d8262c 80%,#b51d22 100%)}
.hero-title{left:62px;top:286px;font-family:"Russo One",sans-serif;line-height:1.05;white-space:nowrap}
.hero-title .a{color:var(--orange);font-size:47px}
.hero-title .b{color:var(--ink);font-size:47px}
.hero-copy{left:62px;top:413px;width:350px;font-size:12.5px;line-height:23px;color:#333}
.btn{display:flex;align-items:center;justify-content:center;background:var(--orange);color:var(--white);font-weight:600;font-size:12.5px;border-radius:24px 0 24px 24px;text-transform:uppercase;white-space:nowrap}
.btn-dark{background:var(--ink);border-radius:8px 0 8px 8px;font-size:10.5px}

/* block plans */
.plans{left:0;top:750px;width:1200px;height:592px;background:linear-gradient(90deg,#f08418 0%,#f7931e 50%,#f6a040 100%)}
.section-title{left:0;width:1200px;font-family:"Montserrat",sans-serif;font-weight:700;font-size:34px}
.plans-intro{left:335px;width:530px;top:874px;font-size:13px;line-height:21px;color:var(--white)}
.hexicon{width:104px;height:96px}
.plan-title{width:300px;font-size:17px;font-weight:500;color:var(--white)}
.plan-text{width:290px;font-size:11.5px;line-height:20.5px;color:#fff3e3}
.arrow{width:38px;height:38px;border:1.5px solid var(--white);border-radius:50%;display:flex;align-items:center;justify-content:center}

/* welcome */
.welcome{left:0;top:1342px;width:1200px;height:780px;background:linear-gradient(180deg,#fbfbfb 0%,#f3f3f3 100%)}
.welcome-copy{left:285px;width:630px;top:1474px;font-size:12px;line-height:21px;color:#9a9a9a}
.card{width:286px;height:304px;background:var(--white);box-shadow:0 0 6px rgba(0,0,0,.12)}
.card .photo{position:absolute;left:8px;top:8px;width:270px;height:194px}
.card p{position:absolute;left:14px;right:14px;top:222px;font-size:12px;line-height:21px;color:#333;text-align:center}

/* drawings */
.plan-drawing{left:135px;top:2196px;width:391px;height:278px;border:6px solid #8f8f8f;background:linear-gradient(135deg,#ffffff 0%,#eeeeee 100%)}
.draw-title{left:616px;top:2193px;font-family:"Montserrat",sans-serif;font-weight:700;font-size:34px;line-height:1.1;color:var(--ink)}
.draw-title em{font-style:normal;color:var(--orange)}
.draw-copy{left:616px;top:2284px;width:450px;font-size:12px;line-height:21px;color:#9a9a9a}

/* footer */
.footer{left:0;top:2549px;width:1200px;height:549px;background:var(--footer)}
.foot-logo{left:0;width:1200px;top:2655px;justify-content:center}
.foot-col{width:260px;font-size:12px;line-height:21px;color:var(--white)}
.foot-ico{width:40px;height:40px;border-radius:50%;background:var(--orange);display:flex;align-items:center;justify-content:center}
.foot-div{width:1px;height:110px;background:var(--line)}
.foot-links{left:367px;top:2875px;width:460px;height:38px;border-top:1px solid var(--line);border-bottom:1px solid var(--line);display:flex;align-items:center;justify-content:center;gap:10px;font-size:12px;color:var(--white);white-space:nowrap}
.copy{left:0;width:1200px;top:2945px;font-size:10px;color:#9c9c9c}
</style>
</head>
<body>

<!-- top bar -->
<div class="abs topbar">
  <div class="item"><span class="ico-hex"><svg width="14" height="14" viewBox="0 0 24 24"><path fill="#fff" d="M6.6 10.8a15 15 0 0 0 6.6 6.6l2.2-2.2c.3-.3.7-.4 1-.2 1.1.4 2.3.6 3.6.6.6 0 1 .4 1 1V20c0 .6-.4 1-1 1A17 17 0 0 1 3 4c0-.6.4-1 1-1h3.5c.6 0 1 .4 1 1 0 1.3.2 2.5.6 3.6.1.3 0 .7-.2 1z"/></svg></span>Call Us &nbsp;: &nbsp;<b>+614 55 210 47, 48 902 361 554</b></div>
  <div class="item"><span class="ico-hex"><svg width="14" height="14" viewBox="0 0 24 24"><path fill="#fff" d="M3 5h18v14H3z"/><path fill="none" stroke="#f7931e" stroke-width="1.8" d="M3 6l9 7 9-7"/></svg></span>Email Us &nbsp;: &nbsp;<b>info@tandaraflame-example.com.au</b></div>
  <div class="item"><div class="social"><span></span><span></span><span></span></div></div>
</div>

<!-- header -->
<div class="abs logo" style="left:60px;top:56px"><span class="dot"></span><span class="name">Tandara Flame</span></div>
<nav class="abs nav">
  <span class="active">HOME</span><span>ABOUT US</span><span>FIRE SERVICES PLANS</span><span>FIRE BLOCK PLANS</span><span>CONTACT US</span>
</nav>
<div class="abs nav-mark"></div>
<svg class="abs search" width="16" height="16" viewBox="0 0 24 24"><circle cx="10" cy="10" r="7" fill="none" stroke="#f7931e" stroke-width="2.4"/><path d="M15 15l6 6" stroke="#f7931e" stroke-width="2.4"/></svg>

<!-- hero -->
<section class="abs hero"></section>
<div class="abs hero-photo" role="img" aria-label="Technician in a cap and checked shirt inspecting a wall-mounted red fire extinguisher with a clipboard"></div>
<h1 class="abs hero-title"><span class="a">TANDARA</span><br><span class="b">FLAME SERVICES</span></h1>
<p class="abs hero-copy">We pride ourselves in our ability to meet the demand of our clients and our ability to consistently uphold our 3 key business values in providing our services at quick turnaround, quality service at competitive pricing.</p>
<a class="abs btn" style="left:60px;top:529px;width:150px;height:45px">Contact Us Now</a>

<!-- fire block plans -->
<section class="abs plans" role="img" aria-label="Orange-toned background of a coiled fire hose reel"></section>
<h2 class="abs section-title center" style="top:822px;color:#fff">FIRE BLOCK PLANS</h2>
<p class="abs plans-intro center">We can can also assist you with the preparation of final commissioning documentation as required to achieve with relevant Australian Standards. Some of the services we provide (but not limited to) include.</p>

<svg class="abs hexicon" style="left:225px;top:968px" viewBox="0 0 104 96"><polygon points="26,2 78,2 102,48 78,94 26,94 2,48" fill="#fff" stroke="#111" stroke-width="3"/><ellipse cx="52" cy="44" rx="26" ry="10" fill="none" stroke="#111" stroke-width="3"/><path d="M28 46v6c0 6 48 6 48 0v-6" fill="none" stroke="#f7931e" stroke-width="3"/><path d="M40 62l-2 6M52 63v7M64 62l2 6" stroke="#f7931e" stroke-width="2.5"/></svg>
<svg class="abs hexicon" style="left:548px;top:968px" viewBox="0 0 104 96"><polygon points="26,2 78,2 102,48 78,94 26,94 2,48" fill="#fff" stroke="#111" stroke-width="3"/><rect x="32" y="20" width="40" height="8" fill="none" stroke="#111" stroke-width="3"/><circle cx="52" cy="38" r="8" fill="none" stroke="#111" stroke-width="3"/><path d="M34 48h36" stroke="#111" stroke-width="3"/><g fill="#f7931e"><circle cx="36" cy="62" r="3"/><circle cx="52" cy="64" r="3"/><circle cx="68" cy="62" r="3"/><circle cx="44" cy="72" r="3"/><circle cx="60" cy="72" r="3"/></g></svg>
<svg class="abs hexicon" style="left:870px;top:968px" viewBox="0 0 104 96"><polygon points="26,2 78,2 102,48 78,94 26,94 2,48" fill="#fff" stroke="#111" stroke-width="3"/><path d="M40 30h24v40H40zM36 74h32M44 22h16v8H44z" fill="none" stroke="#111" stroke-width="3"/><circle cx="52" cy="46" r="6" fill="none" stroke="#f7931e" stroke-width="3"/><path d="M30 42h10v10H30zM64 42h10v10H64z" fill="none" stroke="#f7931e" stroke-width="3"/></svg>

<h3 class="abs plan-title center" style="left:127px;top:1092px">Zone Block Plans</h3>
<h3 class="abs plan-title center" style="left:450px;top:1092px">Sprinkler Block Plans</h3>
<h3 class="abs plan-title center" style="left:772px;top:1092px">Fire Hydrant Block Plans</h3>
<p class="abs plan-text center" style="left:132px;top:1129px">S1670.1 requires an automatic smoke detection and alarm system to incorporate a Zone Block Plan to be securely mounted and easily accessible at the Fire Brigade Panel (FBP).</p>
<p class="abs plan-text center" style="left:455px;top:1129px">AS2118.1 requires Automatic Fire Sprinkler Systems to incorporate a Sprinkler Block Plan to be located adjacent to each set or group of installation control assemblies.</p>
<p class="abs plan-text center" style="left:777px;top:1129px">AS2419.1 requires Fire Hydrant Systems to incorporate a Fire Hydrant Block Plan to be located at the location of fire brigade booster assemblies, fire control rooms and pump rooms.</p>
<a class="abs btn btn-dark" style="left:229px;top:1230px;width:97px;height:32px">LEARN MORE</a>
<a class="abs btn btn-dark" style="left:551px;top:1230px;width:97px;height:32px">LEARN MORE</a>
<a class="abs btn btn-dark" style="left:873px;top:1230px;width:97px;height:32px">LEARN MORE</a>
<div class="abs arrow" style="left:41px;top:1099px"><svg width="12" height="12" viewBox="0 0 12 12"><path d="M8 1L3 6l5 5" fill="none" stroke="#fff" stroke-width="1.6"/></svg></div>
<div class="abs arrow" style="left:1121px;top:1099px"><svg width="12" height="12" viewBox="0 0 12 12"><path d="M4 1l5 5-5 5" fill="none" stroke="#fff" stroke-width="1.6"/></svg></div>

<!-- welcome -->
<section class="abs welcome" role="img" aria-label="Faded background of a fire alarm control room"></section>
<h2 class="abs section-title center" style="top:1412px;color:var(--ink)">WELCOME TO <span style="color:var(--orange)">TANDARA FLAME</span></h2>
<div class="abs welcome-copy center">
  <p>Tandara Flame is a company based in Sydney, Australia providing the Australian market expertise in the field of fire safety. Our mission is to assist our clients with the preparation of design and specifications of fire services upgrades and final commissioning documentation to achieve compliance with the National Construction Code (NCC) and relevant Australian Standards.</p>
  <p style="margin-top:14px">We can also assist with the review and endorsement of fire services design required under the new fire safety reforms which came into effect on July 2017.</p>
</div>
<a class="abs btn" style="left:540px;top:1635px;width:120px;height:45px">Learn More</a>

<div class="abs card" style="left:135px;top:1739px">
  <div class="photo" role="img" aria-label="Technician in a hard hat standing beside an open red fire panel" style="background:linear-gradient(90deg,#b5222a 0%,#d94545 40%,#3a3a3a 70%,#d8d2cc 100%)"></div>
  <p>We pride ourselves on our prompt service and delivery of all of our projects. You can rely on us to meet your project deadlines!</p>
</div>
<div class="abs card" style="left:457px;top:1739px">
  <div class="photo" role="img" aria-label="Technician testing a wall-mounted alarm device" style="background:linear-gradient(90deg,#c9ccc9 0%,#8f2b2b 35%,#d9d9d9 60%,#efefef 100%)"></div>
  <p>Our customer service and our output is guaranteed to be of the highest quality. You will not be disappointed.</p>
</div>
<div class="abs card" style="left:780px;top:1739px">
  <div class="photo" role="img" aria-label="Smiling engineer with arms crossed beside a red fire indicator panel" style="background:linear-gradient(90deg,#f3f3f3 0%,#9fb6d3 35%,#e2e2e2 65%,#c8473f 100%)"></div>
  <p>We strive to always be competitively priced are very competitively priced.</p>
</div>

<!-- drawings -->
<div class="abs plan-drawing" role="img" aria-label="Architectural floor plan with fire services layout"></div>
<h2 class="abs draw-title">FIRE SERVICES<br><em>DRAWINGS</em></h2>
<p class="abs draw-copy">Tandara Flame can assist with the preparation of the design and specification for the upgrade or installation or new fire safety systems to achieve complian -ce with the National Construction Code (NCC), Council Fire Orders or Fire Engineering Reports.We have proficient knowledge in the ability to produce design and specifications relating to the below fire safety measures. Automatic Smoke Detection and Alarm System.</p>
<a class="abs btn" style="left:615px;top:2430px;width:120px;height:45px">Learn More</a>

<!-- footer -->
<footer class="abs footer"></footer>
<div class="abs logo foot-logo"><span class="dot"></span><span class="name" style="font-size:20px">Tandara Flame</span></div>

<div class="abs foot-ico" style="left:257px;top:2742px"><svg width="16" height="18" viewBox="0 0 24 28"><path fill="#fff" d="M12 1a9 9 0 0 0-9 9c0 7 9 17 9 17s9-10 9-17a9 9 0 0 0-9-9z"/><circle cx="12" cy="10" r="3.5" fill="#f7931e"/></svg></div>
<div class="abs foot-ico" style="left:580px;top:2742px"><svg width="16" height="16" viewBox="0 0 24 24"><path fill="#fff" d="M6.6 10.8a15 15 0 0 0 6.6 6.6l2.2-2.2c.3-.3.7-.4 1-.2 1.1.4 2.3.6 3.6.6.6 0 1 .4 1 1V20c0 .6-.4 1-1 1A17 17 0 0 1 3 4c0-.6.4-1 1-1h3.5c.6 0 1 .4 1 1 0 1.3.2 2.5.6 3.6.1.3 0 .7-.2 1z"/></svg></div>
<div class="abs foot-ico" style="left:902px;top:2742px"><svg width="16" height="14" viewBox="0 0 24 20"><path fill="#fff" d="M1 2h22v16H1z"/><path fill="none" stroke="#f7931e" stroke-width="2" d="M1 3l11 8 11-8"/></svg></div>
<div class="abs foot-div" style="left:440px;top:2742px"></div>
<div class="abs foot-div" style="left:762px;top:2742px"></div>
<p class="abs foot-col center" style="left:147px;top:2796px">123,Address,Street Name, State<br>Name City Name, Zipcode.</p>
<p class="abs foot-col center" style="left:470px;top:2796px">ABN : 48 902 361 554<br>M : +614 55 210 478</p>
<p class="abs foot-col center" style="left:792px;top:2796px">E : info@tandaraflame-example.com.au</p>

<nav class="abs foot-links"><span>Home</span>|<span>About Us</span>|<span>Fire Services Plans</span>|<span>Fire Block Plans</span>|<span>Contact Us</span></nav>
<p class="abs copy center">Copyright © TANDARA FLAME - 2021 . All right reserved.</p>
<div class="abs social" style="left:534px;top:2985px;gap:10px"><span style="width:38px;height:38px;background:#4a68b0"></span><span style="width:38px;height:38px"></span><span style="width:38px;height:38px"></span></div>

</body>
</html>
```